Peer-to-peer Car Rental Business needs a business card design

We need a business card design for a new company based in Melbourne, Australia called "Motorvale". We enable car owners to earny money by renting out their car to others in the community/neighbourhood when their not using it.
We would like to see designs that use the colour/s blue and/or orange.
The design should communicate young, modern, fun etc.
The themes to use should be community/neighbourhood, cars, parking, airports, car rental, sharing.

Target Market(s)

Young adults aged 20-35, travellers, environmentally conscious, cost conscious.

Industry/Entity Type

Business

Requirements
Must have
• Must have fields for persons name, title, mobile number, email company website.

```html
<!DOCTYPE html>
<html lang="en">
<head>
<meta charset="utf-8">
<title>Motorvale Business Card</title>
<link rel="stylesheet" href="https://fonts.googleapis.com/css2?family=Poppins:wght@300&family=PT+Sans:wght@400;700&display=swap">
<style>
  :root {
    --page-bg: #e9ebee;
    --brand-blue: #124c80;
    --brand-blue-deep: #0d3a66;
    --brand-blue-soft: #3d6aa6;
    --card-white: #ffffff;
    --text-grey: #555a60;
    --card-shadow: 0 4px 14px rgba(0, 0, 0, 0.25);
  }
  html, body {
    margin: 0;
    padding: 0;
    width: 1200px;
    height: 900px;
    overflow: hidden;
    background: var(--page-bg);
  }
  .canvas {
    position: relative;
    width: 1200px;
    height: 900px;
  }
  .card {
    position: absolute;
    top: 288px;
    width: 570px;
    height: 324px;
    border-radius: 14px;
    overflow: hidden;
    box-shadow: var(--card-shadow);
  }
  .card-front {
    left: 24px;
    background: linear-gradient(120deg, var(--brand-blue) 0%, var(--brand-blue-deep) 100%);
  }
  .card-back {
    left: 606px;
    background: var(--card-white);
  }
  .split-disc {
    position: absolute;
    width: 324px;
    height: 324px;
    border-radius: 50%;
    top: 0;
  }
  .card-front .split-disc {
    left: 406px;
    background: var(--card-white);
  }
  .card-back .split-disc {
    left: -162px;
    background: var(--brand-blue);
  }
  .wordmark {
    position: absolute;
    font-family: "Poppins", sans-serif;
    font-weight: 300;
    line-height: 1;
    white-space: nowrap;
  }
  .card-front .wordmark {
    left: 24px;
    top: 160px;
    font-size: 64px;
    color: var(--card-white);
  }
  .card-back .wordmark {
    right: 22px;
    top: 252px;
    font-size: 46px;
    color: var(--brand-blue-soft);
  }
  .contact-block {
    position: absolute;
    left: 188px;
    top: 28px;
    font-family: "PT Sans", sans-serif;
    color: var(--text-grey);
  }
  .person-name {
    margin: 0;
    font-size: 26px;
    font-weight: 700;
    color: var(--brand-blue);
    line-height: 1.1;
  }
  .person-title {
    margin: 0 0 0 3px;
    font-size: 15px;
    line-height: 1.2;
  }
  .address {
    margin: 22px 0 0 3px;
    font-size: 15px;
    line-height: 1.2;
    font-style: normal;
  }
  .contact-list {
    list-style: none;
    margin: 18px 0 0 3px;
    padding: 0;
    font-size: 15px;
  }
  .contact-list li {
    display: flex;
    align-items: center;
    height: 20.4px;
  }
  .contact-icon {
    width: 10px;
    height: 10px;
    margin-right: 8px;
    fill: var(--brand-blue);
    flex-shrink: 0;
  }
</style>
</head>
<body>
<main class="canvas">
  <section class="card card-front">
    <div class="split-disc"></div>
    <span class="wordmark">Motorvale</span>
  </section>

  <section class="card card-back">
    <div class="split-disc"></div>
    <div class="contact-block">
      <h1 class="person-name">Dylan Marsh</h1>
      <p class="person-title">Managing Member</p>
      <address class="address">218 Laneway Court,<br>Fitzroy, VIC 3065</address>
      <ul class="contact-list">
        <li>
          <svg class="contact-icon" viewBox="0 0 10 10" aria-hidden="true"><path d="M2 0.5 L3.6 2.8 L2.6 3.8 Q3.6 6 6.2 7.4 L7.2 6.4 L9.5 8 L8.2 9.5 Q2.5 8.5 0.5 1.8 Z"/></svg>
          (03) 9417-2284
        </li>
        <li>
          <svg class="contact-icon" viewBox="0 0 10 10" aria-hidden="true"><rect x="2.5" y="0.5" width="5" height="3"/><rect x="0.5" y="4" width="9" height="4"/><rect x="2.5" y="7" width="5" height="2.5"/></svg>
          (03) 9417-2285
        </li>
        <li>
          <svg class="contact-icon" viewBox="0 0 10 10" aria-hidden="true"><path d="M2.5 0 H7.5 V10 H2.5 Z M3.5 1.2 V7.8 H6.5 V1.2 Z"/></svg>
          0412 558 907
        </li>
        <li>
          <svg class="contact-icon" viewBox="0 0 10 10" aria-hidden="true"><path d="M0 2 H10 V8.5 H0 Z"/><path d="M0.5 2.3 L5 5.6 L9.5 2.3" fill="none" stroke="#fff" stroke-width="0.8"/></svg>
          dylan@motorvale.com
        </li>
        <li>
          <svg class="contact-icon" viewBox="0 0 10 10" aria-hidden="true"><circle cx="5" cy="5" r="4.6"/><path d="M0.4 5 H9.6 M5 0.4 V9.6 M5 0.4 Q2 5 5 9.6 M5 0.4 Q8 5 5 9.6" fill="none" stroke="#fff" stroke-width="0.6"/></svg>
          www.motorvale.com
        </li>
      </ul>
    </div>
    <span class="wordmark">Motorvale</span>
  </section>
</main>
</body>
</html>
```